a book cover featuring an american west vibe and the image of a coyote.
The author is Walter Brantley
It needs to say "Meridian Dispatch Bestselling Author" above his name.
It needs to have "Introduction by Dean Brantley" in smaller type (perhaps as a round "sticker" to go on the cover as an added element.
The book is called
Ashes of Red Mesa
there will be a subtitle
Where the prairie kept its own quiet laws
I'm looking for a gorgeous and elegant type. I've attached a couple of samples.
I want to thank everyone who contributed a design. It was very difficult to choose. In fact, the family of the author made the final decision and I think they chose well too. I was overwhelmed by the quality of your work.

```html
<!DOCTYPE html>
<html lang="en">
<head>
<meta charset="utf-8">
<title>Ashes of Red Mesa — Walter Brantley</title>
<link rel="stylesheet" href="https://fonts.googleapis.com/css2?family=Cinzel:wght@400;500&family=Open+Sans:wght@400;600&display=swap">
<style>
  :root {
    --sky-top: #163a86;
    --sky-mid: #3f6fc0;
    --sky-low: #a9c3e0;
    --ground-far: #b99a62;
    --ground-near: #8a5a26;
    --fur-light: #c9a878;
    --fur-dark: #6e5233;
    --ink-white: #ffffff;
    --sticker-ring: #cfd2d6;
    --sticker-face: #ffffff;
    --sticker-ink: #1d1d1d;
    --sticker-accent: #3d5f9a;
  }
  html, body { margin: 0; padding: 0; overflow: hidden; background: #222; }
  .cover {
    position: relative;
    width: 749px;
    height: 1200px;
    overflow: hidden;
    font-family: "Open Sans", Arial, sans-serif;
    color: var(--ink-white);
  }
  .cover__scene { position: absolute; inset: 0; }
  .cover__text { position: absolute; left: 0; right: 0; text-align: center; text-shadow: 0 2px 6px rgba(0,0,0,.35); }
  .author-credit {
    top: 62px;
    font-size: 25px;
    font-weight: 400;
    letter-spacing: 2.5px;
    text-transform: uppercase;
  }
  .author-name {
    top: 104px;
    font-family: "Cinzel", "Times New Roman", serif;
    font-size: 82px;
    font-weight: 400;
    letter-spacing: 1px;
  }
  .book-title { top: 288px; font-family: "Cinzel", "Times New Roman", serif; font-weight: 400; text-transform: uppercase; }
  .book-title__lead { display: block; font-size: 48px; line-height: 56px; }
  .book-title__main { display: block; font-size: 98px; line-height: 112px; }
  .subtitle {
    top: 496px;
    font-size: 29px;
    line-height: 38px;
  }
  .sticker {
    position: absolute;
    left: 62px;
    top: 954px;
    width: 188px;
    height: 188px;
    border-radius: 50%;
    background: radial-gradient(circle at 35% 30%, #ffffff, var(--sticker-ring) 70%, #9ea3a8);
    box-shadow: 0 4px 10px rgba(0,0,0,.35);
    display: flex;
    align-items: center;
    justify-content: center;
  }
  .sticker__face {
    width: 160px;
    height: 160px;
    border-radius: 50%;
    background: var(--sticker-face);
    color: var(--sticker-ink);
    display: flex;
    flex-direction: column;
    align-items: center;
    justify-content: center;
    text-align: center;
    line-height: 1.15;
  }
  .sticker__intro { font-size: 13px; margin-bottom: 6px; }
  .sticker__outlet { font-size: 17px; font-weight: 600; }
  .sticker__role { font-size: 13px; }
  .sticker__name { font-size: 14px; color: var(--sticker-accent); margin-top: 6px; letter-spacing: .5px; text-transform: uppercase; }
</style>
</head>
<body>
<main class="cover">
  <svg class="cover__scene" width="749" height="1200" viewBox="0 0 749 1200" role="img" aria-label="Photograph of a coyote standing on a dry golden prairie under a deep blue sky with scattered clouds and distant farm buildings">
    <defs>
      <linearGradient id="sky" x1="0" y1="0" x2="0" y2="1">
        <stop offset="0" stop-color="var(--sky-top)"/>
        <stop offset=".55" stop-color="var(--sky-mid)"/>
        <stop offset="1" stop-color="var(--sky-low)"/>
      </linearGradient>
      <linearGradient id="ground" x1="0" y1="0" x2="0" y2="1">
        <stop offset="0" stop-color="var(--ground-far)"/>
        <stop offset="1" stop-color="var(--ground-near)"/>
      </linearGradient>
      <radialGradient id="animal" cx=".5" cy=".45" r=".55">
        <stop offset="0" stop-color="var(--fur-light)"/>
        <stop offset=".7" stop-color="var(--fur-dark)" stop-opacity=".55"/>
        <stop offset="1" stop-color="var(--fur-dark)" stop-opacity="0"/>
      </radialGradient>
    </defs>
    <rect width="749" height="845" fill="url(#sky)"/>
    <rect y="840" width="749" height="360" fill="url(#ground)"/>
    <rect x="210" y="665" width="420" height="480" rx="120" fill="url(#animal)"/>
  </svg>

  <p class="cover__text author-credit" style="margin:0">Meridian Dispatch Bestselling Author</p>
  <h2 class="cover__text author-name" style="margin:0">Walter Brantley</h2>
  <h1 class="cover__text book-title" style="margin:0">
    <span class="book-title__lead">Ashes of</span>
    <span class="book-title__main">Red Mesa</span>
  </h1>
  <p class="cover__text subtitle" style="margin:0">Where the prairie kept its own<br>quiet laws</p>

  <aside class="sticker">
    <div class="sticker__face">
      <span class="sticker__intro">Introduction By</span>
      <span class="sticker__outlet">Meridian Dispatch</span>
      <span class="sticker__role">Bestselling Author</span>
      <span class="sticker__name">Dean Brantley</span>
    </div>
  </aside>
</main>
</body>
</html>
```